Marrowby's Vacation Rentals Business Card

Multi Million dollar villa rentals in the Dominican Republic.

Industry/Entity Type

Business

Contact Information for Business Card

I am looking for a high-end look around my company name/logo (see attached) on one side incorporating the following info: first and last name, title, address, phone #, email and company website. On the backside I want to add a full color picture of one of our villas (see attached).

```html
<!DOCTYPE html>
<html lang="en">
<head>
<meta charset="utf-8">
<title>Marrowby's Vacation Rentals – Business Card</title>
<link rel="stylesheet" href="https://fonts.googleapis.com/css2?family=Questrial&display=swap">
<style>
  :root {
    --page-bg: #e2e2e2;
    --card-white: #ffffff;
    --ink: #111111;
    --ink-soft: #333333;
    --pool-blue: #1aa3e0;
    --pool-deep: #0f8fd0;
    --sky: #8fbde6;
    --villa: #e9e3d6;
    --foliage: #3d6b33;
    --accent-orange: #f07a2a;
    --icon-blue: #2a7fc7;
  }
  * { margin: 0; padding: 0; box-sizing: border-box; }
  html, body { width: 1200px; height: 900px; overflow: hidden; }
  body {
    background: var(--page-bg);
    font-family: "Questrial", "Century Gothic", sans-serif;
    color: var(--ink);
    position: relative;
  }
  .card {
    position: absolute;
    left: 336px;
    width: 530px;
    height: 318px;
    overflow: hidden;
  }
  .card--front { top: 111px; }
  .card--back { top: 462px; background: var(--card-white); }

  .villa-photo {
    position: absolute;
    inset: 0;
    background: linear-gradient(180deg,
      var(--sky) 0%,
      var(--foliage) 14%,
      var(--villa) 28%,
      var(--villa) 46%,
      #b9b3a6 54%,
      var(--pool-blue) 60%,
      var(--pool-deep) 100%);
  }
  .front-url {
    position: absolute;
    right: 30px;
    bottom: 19px;
    color: #ffffff;
    font-size: 14px;
    letter-spacing: 2.6px;
  }

  .brand {
    position: absolute;
    left: 70px;
    top: 145px;
    width: 200px;
    display: flex;
    align-items: center;
    gap: 6px;
  }
  .brand-dot {
    flex: none;
    width: 12px; height: 12px;
    border-radius: 50%;
    background: var(--accent-orange);
  }
  .brand-name {
    font-size: 14px;
    color: var(--ink);
    white-space: nowrap;
  }
  .divider {
    position: absolute;
    left: 291px;
    top: 91px;
    width: 2px;
    height: 134px;
    background: var(--ink);
  }
  .person {
    position: absolute;
    left: 316px;
    top: 104px;
  }
  .person-name { font-size: 19px; line-height: 1.1; letter-spacing: 0.3px; font-weight: 400; }
  .person-title { font-size: 10px; color: var(--ink-soft); margin-top: 1px; }
  .contacts {
    position: absolute;
    left: 316px;
    top: 159px;
    list-style: none;
    font-size: 11px;
    line-height: 13px;
    letter-spacing: 0.4px;
  }
  .contacts li { display: flex; align-items: center; gap: 4px; white-space: nowrap; }
  .contacts li.gap { margin-top: 4px; }
  .contacts svg { width: 7px; height: 8px; fill: none; stroke: var(--icon-blue); stroke-width: 1.3; }
</style>
</head>
<body>
  <section class="card card--front">
    <div class="villa-photo" role="img" aria-label="Photograph of a white villa with terracotta roof and palm trees behind a bright blue swimming pool with blue loungers"></div>
    <p class="front-url">www.marrowbys.com</p>
  </section>

  <section class="card card--back">
    <div class="brand">
      <span class="brand-dot"></span>
      <span class="brand-name">Marrowby's Vacation Rentals</span>
    </div>
    <div class="divider"></div>
    <div class="person">
      <h1 class="person-name">E Marrowby</h1>
      <p class="person-title">Manager</p>
    </div>
    <ul class="contacts">
      <li><svg viewBox="0 0 8 8"><path d="M1.5 1 L3 1 L3.5 2.6 L2.6 3.3 Q3.5 5 5 5.6 L5.6 4.6 L7 5 L7 6.6 Q3 7 1.2 2 Z"/></svg>560.555.0142</li>
      <li><svg viewBox="0 0 8 8"><rect x="2" y="0.7" width="4" height="6.6" rx="0.6"/></svg>560.555.0187</li>
      <li class="gap"><svg viewBox="0 0 8 8"><rect x="0.7" y="2" width="6.6" height="4.2" fill="var(--icon-blue)"/></svg>info@marrowbys.com</li>
      <li><svg viewBox="0 0 8 8"><circle cx="4" cy="4" r="3.2"/><path d="M0.8 4 H7.2 M4 0.8 Q2 4 4 7.2 Q6 4 4 0.8"/></svg>www.marrowbys.com</li>
    </ul>
  </section>
</body>
</html>
```